Vornelle Distance Learning Website

Vornelle provide e-learning and mixed learning solutions for individuals, colleges, organisations and B2B.
We need a modern, light and flat website design for Vornelle. We want to to see the designer incorporate user experience(UX) design elements into the AI or PSD mockups. We would like to see designs that use pastel colors that compliment yellow and black of our logo.
We want our E-learning experience to accelerate learning and for the interface to be user friendly and intuitive. We want the designs to focus on quick access to course information, course reviews, learning progress and study advice. Quick and intuitive access to all content for our clients is one of our top priorities.
We would like designs for the following project 3 pages:
1. Learner homepage dashboard (see attached screenshot).
On this page the Learners need to:
- Login
- Have quick access to Packages and Courses.
- See other recommended courses (Below Packages and Courses)
- Possibly a left hand side column/menu with thumbnail icons (See quillory learner dashboard screenshot)
2. Homepage
See current sample
http://www.vornelle-learn.test
We would like the designer to focus on creating a customized banner to enhance the home page.
3. Primary Landing/Marketing page
This page is geared towards customer acquisition with the focal point being the top banner (video or HD image).
And Course Preview content below.
See reference
http://vornelle-learn.test/subscriptionPlans/marketing/MTc%3D/Mjc4Nw%3D%3D/Mastering%20Dorvish%20%2B%20Dorvish%20Nibbles%20Bundle%20by%20Gideon%20Pell%20Mawry
Other site we like:
- https://www.brenvato.test (We like the home page and top bar on courses page)
- http://www.pollenhallstudy.test
- http://crestfoldlabs.test (think this site looks great, love the lower graphics on the homepage)
Updates
Hello,
Thank you for taking the time to contribute to this web design competition. We would just like to point out a few things:
1. Please try to make the color palette similar to the colors used in the screenshot that we just uploaded ('possible color palette).
2. Please make the designs specific to each page: THE LEARNER HOMEPAGE, HOME PAGE, and the MARKETING LANDING PAGE.
We are very happy with the high quality of designs so far,
Cheers,
Len Fa
KV-Studio
Also,
Please avoid using dark/bold elements in the designs. The ONLY elements that we want to be dark are the logo and the footer.
Any questions please ask,
Cheers,
Len Fa
Kv-Studio
Hello,
Based on the round of feedback we just gave it would be great if you could complete further design changes by tomorrow, as we are pushed for time.
Thank you,
Len Fa
KV-Studio

```html
<!DOCTYPE html>
<html lang="en">
<head>
<meta charset="utf-8">
<title>Vornelle – Learner Dashboard</title>
<link rel="stylesheet" href="https://fonts.googleapis.com/css2?family=Signika:wght@300;400;600&family=Arimo:wght@400;700&display=swap">
<style>
:root{
  --sidebar:#dfdfdf;
  --page:#ffffff;
  --band:#e6e6e6;
  --field:#ececec;
  --text:#555555;
  --muted:#9a9a9a;
  --faint:#b5b5b5;
  --accent:#f5b21b;
  --accent-soft:#f8d27a;
  --accent-mid:#f5be3c;
  --blue:#6bb0e0;
  --teal:#1fb89a;
  --alert:#e8533a;
  --button:#a9a49f;
  --white:#ffffff;
}
*{box-sizing:border-box;margin:0;padding:0}
html,body{width:871px;height:1200px;overflow:hidden}
body{position:relative;background:var(--page);font-family:"Signika",sans-serif;color:var(--text)}
.abs{position:absolute}

/* sidebar */
.sidebar{left:0;top:0;width:207px;height:1200px;background:var(--sidebar)}
.menu-toggle{left:16px;top:15px;width:30px;height:30px}
.active-bar{left:0;top:57px;width:6px;height:118px;background:var(--accent)}
.nav-item{left:43px;font-size:10px;font-weight:600;color:var(--muted);letter-spacing:.3px}
.nav-icon{left:22px;width:12px;height:11px}
.nav-sub{left:50px;font-size:7px;color:var(--muted)}
.badge{left:178px;width:13px;height:13px;border-radius:50%;background:#b8b8b8;color:var(--white);font-size:6.5px;text-align:center;line-height:13px;font-weight:600}
.badge.alert{background:var(--alert)}

/* header */
.brand{left:228px;top:19px;display:flex;align-items:center;gap:6px;font-size:21px;font-weight:600;color:#222}
.brand-dot{width:12px;height:12px;background:var(--accent);border-radius:50%}
.search{left:328px;top:19px;width:198px;height:24px;border:2px solid var(--field);border-radius:2px;font-size:6px;color:var(--muted);padding:7px 0 0 22px}
.search svg{position:absolute;left:8px;top:6px}
.top-link{top:27px;font-size:8px;color:var(--muted)}
.top-badge{left:738px;top:24px;width:8px;height:8px;border-radius:50%;background:var(--alert);color:#fff;font-size:4px;text-align:center;line-height:8px}
.user-avatar{left:763px;top:22px;width:19px;height:19px;border-radius:50%;background:linear-gradient(#8a5b48,#c99b83)}

/* tiles */
.tile{top:75px;height:105px;display:flex;flex-direction:column;align-items:center;color:var(--white);font-size:8.5px;text-align:center;line-height:1.15}
.tile svg{margin-top:20px;height:34px}
.tile span{position:absolute;bottom:26px}

/* profile */
.cover{left:218px;top:193px;width:311px;height:182px;background:linear-gradient(120deg,#4e5a66 0%,#6f6a63 40%,#a48c6e 75%,#c8b79d 100%)}
.cover-name{left:218px;top:218px;width:311px;text-align:center;color:#fff;font-size:14px}
.cover-text{left:250px;top:249px;width:250px;text-align:center;color:#fff;font-size:7.5px;line-height:14px}
.plus-btn{width:20px;height:20px;background:var(--accent);color:#fff;text-align:center;font-size:15px;line-height:19px}
.avatar{left:326px;top:305px;width:101px;height:101px;border-radius:50%;border:4px solid #fff;background:linear-gradient(160deg,#6d6a66,#b5a999 60%,#5a5e64)}
.stat{top:422px;width:80px;text-align:center;font-size:12.5px;color:#444;line-height:19px}
.stat b{font-weight:400;font-size:13.5px}

/* panels */
.band{height:32px;background:var(--band);font-size:7.5px;color:var(--text);padding-left:13px;line-height:32px}
.row{left:559px;width:283px;height:31px;background:#eeeeee;font-size:9px;color:#555;display:flex;align-items:center;gap:11px;padding-left:10px}
.check{width:13px;height:13px;background:var(--accent);display:flex;align-items:center;justify-content:center}
.check.grey{background:#a5a5a5}
.note{left:559px;top:314px;width:283px;height:99px;background:#eeeeee;font-size:7px;color:var(--muted);padding:12px 13px}
.btn{background:var(--button);color:#fff;text-align:center}

/* chart */
.legend{left:521px;font-size:6.5px;color:var(--blue);display:flex;align-items:center;gap:8px}
.legend i{display:block;width:12px;height:4px;border-radius:1px}
.ring-label{top:814px;width:80px;text-align:center;font-size:6.5px;color:var(--faint)}

/* tracker */
.todo{left:663px;display:flex;align-items:center;gap:13px;font-size:6.5px;color:var(--muted)}
.box{width:12px;height:12px;border:1px solid #cfcfcf}

/* cards */
.card{top:920px;width:149px;height:196px;border:1px solid #bdbdbd;border-radius:3px;overflow:hidden;font-family:"Arimo",sans-serif;background:#fff}
.card-media{height:86px;display:flex;align-items:center;justify-content:center;position:relative}
.card-plus{position:absolute;right:7px;top:7px;width:13px;height:13px;background:#a9a9a9;color:#fff;font-size:11px;line-height:12px;text-align:center}
.card-title{font-size:8px;font-weight:700;color:#555;padding:11px 5px 0;line-height:13px}
.card-author{font-size:8px;color:#666;padding:10px 5px 0}
.card-date{font-size:6.5px;color:#777;padding:16px 5px 4px;border-bottom:1px solid #ccc}
.card-foot{display:flex;align-items:center;padding:5px 5px 0;font-size:7px;color:#666;gap:4px}
.price{margin-left:auto;color:var(--accent);font-size:17px;font-weight:700}
.dot{top:1151px;width:12px;height:12px;border-radius:50%;background:#a39d98}
</style>
</head>
<body>

<aside class="abs sidebar">
  <svg class="abs menu-toggle" viewBox="0 0 30 30"><polygon points="15,1 28,8 28,22 15,29 2,22 2,8" fill="#b3b3b3"/><path d="M9 11h12M9 15h12M9 19h12" stroke="#fff" stroke-width="1.6"/></svg>
  <div class="abs active-bar"></div>

  <svg class="abs nav-icon" style="top:82px" viewBox="0 0 12 11"><path d="M1 6l5-5 5 5v5H1z" fill="#c8c8c8"/></svg>
  <div class="abs nav-item" style="top:81px">Dashboard</div>
  <div class="abs badge alert" style="top:81px">16</div>
  <div class="abs nav-sub" style="top:106px">Learning Publisher Dashboard</div>
  <div class="abs nav-sub" style="top:124px">General settings</div>
  <div class="abs nav-sub" style="top:142px">Help</div>

  <svg class="abs nav-icon" style="top:189px" viewBox="0 0 12 11"><rect x="0.5" y="0.5" width="11" height="10" fill="none" stroke="#c8c8c8"/><path d="M0 3h12" stroke="#c8c8c8"/></svg>
  <div class="abs nav-item" style="top:189px">Find Learning Packages</div>
  <div class="abs badge" style="top:188px">95</div>

  <svg class="abs nav-icon" style="top:227px" viewBox="0 0 12 11"><rect x="0.5" y="0.5" width="8" height="6" fill="none" stroke="#c8c8c8"/><rect x="3.5" y="4.5" width="8" height="6" fill="none" stroke="#c8c8c8"/></svg>
  <div class="abs nav-item" style="top:227px">Reviews and Coments</div>
  <div class="abs badge" style="top:227px">7</div>

  <svg class="abs nav-icon" style="top:266px" viewBox="0 0 12 11"><circle cx="6" cy="5.5" r="5" fill="none" stroke="#c8c8c8"/><path d="M6 5.5V0.5A5 5 0 0 1 11 5.5z" fill="#c8c8c8"/></svg>
  <div class="abs nav-item" style="top:266px">Purchase History</div>
  <div class="abs badge" style="top:266px">7</div>

  <svg class="abs nav-icon" style="top:304px" viewBox="0 0 12 11"><path d="M0.5 0v10.5H12M1 9l3-4 3 2 4-5" fill="none" stroke="#c8c8c8"/></svg>
  <div class="abs nav-item" style="top:304px">Statistic Charts</div>
  <div class="abs badge" style="top:304px">6</div>
</aside>

<header>
  <div class="abs brand"><span class="brand-dot"></span>Vornelle</div>
  <div class="abs search"><svg width="8" height="8" viewBox="0 0 8 8"><circle cx="3.2" cy="3.2" r="2.5" fill="none" stroke="#999"/><path d="M5 5l2.5 2.5" stroke="#999"/></svg>Search for courses</div>
  <div class="abs top-link" style="left:641px">Activity</div>
  <div class="abs top-link" style="left:691px">Notifications</div>
  <div class="abs top-badge">15</div>
  <div class="abs user-avatar" role="img" aria-label="Portrait of the signed-in learner"></div>
  <div class="abs top-link" style="left:788px">Tobin Hartwell</div>
  <svg class="abs" style="left:850px;top:30px" width="7" height="5" viewBox="0 0 7 5"><path d="M0 0h7L3.5 5z" fill="#aaa"/></svg>
</header>

<nav>
  <div class="abs tile" style="left:219px;width:105px;background:#a9a9a9">
    <svg width="38" viewBox="0 0 38 34"><path d="M2 12h34l-4 20H6z" fill="none" stroke="#fff" stroke-width="2"/><path d="M11 12l6-9M27 12l-6-9" stroke="#fff" stroke-width="2"/><path d="M12 17v11M19 17v11M26 17v11" stroke="#fff" stroke-width="2"/></svg>
    <span>Store</span></div>
  <div class="abs tile" style="left:324px;width:107px;background:#9e9e9e">
    <svg width="38" viewBox="0 0 38 34"><path d="M3 4h12l3 3h15v22H3z" fill="none" stroke="#fff" stroke-width="2"/><path d="M7 11h22M7 15h14" stroke="#fff" stroke-width="2"/><path d="M27 33l-8-7a4.5 4.5 0 0 1 8-5 4.5 4.5 0 0 1 8 5z" fill="#fff"/></svg>
    <span>Subscribed<br>Learning Packages</span></div>
  <div class="abs tile" style="left:431px;width:107px;background:#ababab">
    <svg width="38" viewBox="0 0 38 34"><rect x="6" y="3" width="22" height="28" fill="none" stroke="#fff" stroke-width="2"/><path d="M10 10h10M10 15h10M10 20h8M10 25h10" stroke="#fff" stroke-width="2"/><path d="M34 2l-12 18" stroke="#fff" stroke-width="3"/></svg>
    <span>My<br>Published Packages</span></div>
  <div class="abs tile" style="left:538px;width:106px;background:#b3b3b3">
    <svg width="34" viewBox="0 0 34 34"><polygon points="17,1 21.5,12 33,12 23.5,19.5 27,32 17,24.5 7,32 10.5,19.5 1,12 12.5,12" fill="#fff"/></svg>
    <span>Bookmarks</span></div>
  <div class="abs tile" style="left:644px;width:104px;background:#bebebe">
    <svg width="38" viewBox="0 0 38 34"><path d="M9 2h20l7 9-17 21L2 11z M2 11h34 M13 11l6 21 6-21 M9 2l4 9 6-9 6 9 4-9" fill="none" stroke="#fff" stroke-width="1.5"/></svg>
    <span>My VRewards</span></div>
  <div class="abs tile" style="left:748px;width:107px;background:#cbcbcb">
    <svg width="30" viewBox="0 0 30 34"><path d="M12 4H3v26h9" fill="none" stroke="#fff" stroke-width="2.5"/><path d="M10 17h17M21 11l6 6-6 6" fill="none" stroke="#fff" stroke-width="2.5"/></svg>
    <span>Logout account</span></div>
</nav>

<section>
  <div class="abs cover" role="img" aria-label="Photo of a laptop, open book and coffee cup on a desk"></div>
  <div class="abs cover-name">Corin Aldous</div>
  <div class="abs cover-text">Cras et neque vel nunc aliquet dictum vitae eget velit. Maecenas lobortis leo eu odio viverra pulvinar.</div>
  <div class="abs plus-btn" style="left:495px;top:202px">+</div>
  <div class="abs avatar" role="img" aria-label="Profile portrait of the learner"></div>
  <div class="abs stat" style="left:254px">Attended<br><b>17</b></div>
  <div class="abs stat" style="left:338px">Attending<br><b>3</b></div>
  <div class="abs stat" style="left:412px">Notes<br><b>260</b></div>
</section>

<section>
  <div class="abs band" style="left:545px;top:193px;width:311px">Courses in Package</div>
  <div class="abs row" style="top:236px"><span class="check"><svg width="8" height="6" viewBox="0 0 8 6"><path d="M1 3l2 2 4-4" fill="none" stroke="#fff" stroke-width="1.4"/></svg></span>Mastering Dorvish + Dorvish Nibbles Bundle By Gideon Pell Mawry</div>
  <div class="abs row" style="top:273px;font-size:7px;color:#888"><span class="check grey"><svg width="7" height="7" viewBox="0 0 7 7"><path d="M3.5 0v7M0 3.5h7" stroke="#fff" stroke-width="1.4"/></svg></span>Add More Packages</div>
  <div class="abs note">Your note here</div>
  <div class="abs btn" style="left:765px;top:430px;width:77px;height:25px;font-size:8px;line-height:25px">Add Note</div>
</section>

<section>
  <div class="abs band" style="left:219px;top:470px;width:418px">Quick statistics</div>
  <div class="abs legend" style="top:509px"><i style="background:var(--blue)"></i>ipsum dolor sit amet</div>
  <div class="abs legend" style="top:520px;color:var(--accent)"><i style="background:var(--accent)"></i>consectetur adipiscing elit</div>
  <svg class="abs" style="left:219px;top:532px" width="418" height="160" viewBox="219 532 418 160" font-family="Signika, sans-serif" font-size="7" fill="#666">
    <g stroke="#ececec" stroke-width="1">
      <path d="M262 542H620M262 564H620M262 586H620M262 607H620M262 629H620M262 651H620M262 673H620"/>
      <path d="M262 542V673M306 542V673M350 542V673M394 542V673M438 542V673M482 542V673M526 542V673M570 542V673M614 542V673"/>
    </g>
    <g text-anchor="end">
      <text x="255" y="545">300</text><text x="255" y="567">250</text><text x="255" y="589">200</text><text x="255" y="610">150</text><text x="255" y="632">100</text><text x="255" y="654">50</text><text x="255" y="676">0</text>
    </g>
    <g text-anchor="middle">
      <text x="292" y="680">1</text><text x="336" y="680">2</text><text x="380" y="680">3</text><text x="424" y="680">4</text><text x="468" y="680">5</text><text x="512" y="680">6</text><text x="556" y="680">7</text><text x="600" y="680">8</text>
    </g>
    <polyline points="265,592 348,617 418,578 490,602 555,578 616,569" fill="none" stroke="var(--blue)" stroke-width="2"/>
    <polyline points="265,660 327,645 388,652 466,630 512,619 537,567 596,554 617,545" fill="none" stroke="var(--accent)" stroke-width="2"/>
    <g fill="var(--blue)" stroke="#fff" stroke-width="1.5">
      <circle cx="265" cy="592" r="5"/><circle cx="348" cy="617" r="5"/><circle cx="418" cy="578" r="5"/><circle cx="490" cy="602" r="5"/><circle cx="555" cy="578" r="5"/><circle cx="616" cy="569" r="5"/>
    </g>
    <g fill="var(--accent)" stroke="#fff" stroke-width="1.5">
      <circle cx="265" cy="660" r="5"/><circle cx="327" cy="645" r="5"/><circle cx="388" cy="652" r="5"/><circle cx="466" cy="630" r="5"/><circle cx="512" cy="619" r="5"/><circle cx="537" cy="567" r="5"/><circle cx="596" cy="554" r="5"/><circle cx="617" cy="545" r="5"/>
    </g>
  </svg>

  <svg class="abs" style="left:290px;top:746px" width="280" height="66" viewBox="290 746 280 66" font-family="Signika, sans-serif" font-size="12" text-anchor="middle">
    <circle cx="323" cy="779" r="29" fill="none" stroke="#e8e8e8" stroke-width="5"/>
    <circle cx="323" cy="779" r="29" fill="none" stroke="var(--blue)" stroke-width="5" stroke-dasharray="154.9 182.2" transform="rotate(-90 323 779)"/>
    <text x="323" y="783" fill="#999">85%</text>
    <circle cx="429" cy="779" r="29" fill="none" stroke="#e8e8e8" stroke-width="5"/>
    <circle cx="429" cy="779" r="29" fill="none" stroke="var(--accent)" stroke-width="5" stroke-dasharray="118.4 182.2" transform="rotate(-90 429 779)"/>
    <text x="429" y="783" fill="#999">65%</text>
    <circle cx="535" cy="779" r="29" fill="none" stroke="#e8e8e8" stroke-width="5"/>
    <circle cx="535" cy="779" r="29" fill="none" stroke="var(--teal)" stroke-width="5" stroke-dasharray="145.8 182.2" transform="rotate(-90 535 779)"/>
    <text x="535" y="783" fill="#999">80%</text>
  </svg>
  <div class="abs ring-label" style="left:283px">Web design</div>
  <div class="abs ring-label" style="left:389px">Branding design</div>
  <div class="abs ring-label" style="left:495px">Time management</div>
</section>

<section>
  <div class="abs band" style="left:651px;top:470px;width:199px;padding-left:44px">Course Tracker - Todo list</div>
  <div class="abs plus-btn" style="left:662px;top:475px;width:22px;height:22px">+</div>
  <div class="abs" style="left:663px;top:511px;width:174px;height:22px;background:#eeeeee"></div>
  <div class="abs todo" style="top:546px"><span class="check" style="width:12px;height:12px"><svg width="8" height="6" viewBox="0 0 8 6"><path d="M1 3l2 2 4-4" fill="none" stroke="#fff" stroke-width="1.4"/></svg></span>Aliquam metus neque</div>
  <div class="abs todo" style="top:566px"><span class="box"></span>In ut turpis non ipsum rhoncus porttitor</div>
  <div class="abs todo" style="top:585px"><span class="box"></span>Maecenas interdum dignissim</div>
  <div class="abs todo" style="top:604px"><span class="box"></span>Pellentesque sodales ipsum et enim</div>
  <div class="abs todo" style="top:624px"><span class="box"></span>Quisque tincidunt mattis sapien</div>

  <div class="abs band" style="left:651px;top:661px;width:200px">Cloud storage usage</div>
  <svg class="abs" style="left:655px;top:712px" width="196" height="124" viewBox="655 712 196 124" font-family="Signika, sans-serif">
    <circle cx="751" cy="774" r="45" fill="none" stroke="#ececec" stroke-width="19"/>
    <circle cx="751" cy="774" r="45" fill="none" stroke="var(--blue)" stroke-width="19" stroke-dasharray="155 282.7" transform="rotate(-90 751 774)"/>
    <text x="751" y="776" text-anchor="middle" font-size="14" fill="#666">140 / 512</text>
    <text x="751" y="794" text-anchor="middle" font-size="13" fill="#666">GB</text>
    <path d="M697 776H676V806H700" fill="none" stroke="#999" stroke-width="0.8"/>
    <path d="M790 734H824V758" fill="none" stroke="#999" stroke-width="0.8"/>
    <text x="662" y="770" font-size="5.5" fill="#777">Free space</text>
    <text x="812" y="767" font-size="5.5" fill="#777">Storage use</text>
  </svg>
</section>

<section>
  <div class="abs band" style="left:219px;top:864px;width:418px">Recommended  Packages and Courses</div>
  <div class="abs btn" style="left:651px;top:852px;width:200px;height:44px;font-size:10px;line-height:44px;text-align:left;padding-left:14px">Show my files
    <svg class="abs" style="right:14px;top:16px" width="7" height="12" viewBox="0 0 7 12"><path d="M1 1l5 5-5 5" fill="none" stroke="#fff" stroke-width="1.5"/></svg></div>

  <article class="abs card" style="left:221px">
    <div class="card-media" style="background:linear-gradient(#e78a2a,#c86a1c 60%,#3b2a20)" role="img" aria-label="Photo of a statue silhouetted against an orange sunset"><span class="card-plus">+</span></div>
    <div class="card-title">Cras scelerisque et ante eget lacinia iaculis ullamcorper augue.</div>
    <div class="card-author">Mr Alden Frey</div>
    <div class="card-date">12th August 2013</div>
    <div class="card-foot"><svg width="11" height="7" viewBox="0 0 11 7"><path d="M0 3.5Q5.5-2 11 3.5Q5.5 9 0 3.5z" fill="#666"/><circle cx="5.5" cy="3.5" r="1.6" fill="#fff"/></svg>102 <svg style="margin-left:6px" width="9" height="9" viewBox="0 0 10 10"><polygon points="5,0 6.3,3.5 10,3.6 7,5.9 8.1,9.6 5,7.4 1.9,9.6 3,5.9 0,3.6 3.7,3.5" fill="#666"/></svg>4.6<span class="price">50$</span></div>
  </article>

  <article class="abs card" style="left:381px">
    <div class="card-media" style="background:var(--accent-mid)"><span class="card-plus">+</span>
      <svg width="46" height="26" viewBox="0 0 46 26"><path d="M14 2h30v22H14z" fill="#fff"/><path d="M14 2l15 12 15-12" fill="none" stroke="var(--accent-mid)" stroke-width="2"/><path d="M0 8h10M3 13h8M6 18h6" stroke="#fff" stroke-width="2"/></svg></div>
    <div class="card-title">Cras scelerisque et ante eget lacinia iaculis ullamcorper augue.</div>
    <div class="card-author">Mr Alden Frey</div>
    <div class="card-date">12th August 2013</div>
    <div class="card-foot"><svg width="11" height="7" viewBox="0 0 11 7"><path d="M0 3.5Q5.5-2 11 3.5Q5.5 9 0 3.5z" fill="#666"/><circle cx="5.5" cy="3.5" r="1.6" fill="#fff"/></svg>102 <svg style="margin-left:6px" width="9" height="9" viewBox="0 0 10 10"><polygon points="5,0 6.3,3.5 10,3.6 7,5.9 8.1,9.6 5,7.4 1.9,9.6 3,5.9 0,3.6 3.7,3.5" fill="#666"/></svg>4.6<span class="price">75$</span></div>
  </article>

  <article class="abs card" style="left:543px">
    <div class="card-media" style="background:var(--accent)"><span class="card-plus">+</span>
      <svg width="30" height="32" viewBox="0 0 30 32"><path d="M10 1h10M12 1v10L2 29q0 2 2 2h22q2 0 2-2L18 11V1" fill="#fff"/><circle cx="13" cy="23" r="2" fill="var(--accent)"/><circle cx="18" cy="26" r="1.4" fill="var(--accent)"/></svg></div>
    <div class="card-title">Cras scelerisque et ante eget lacinia iaculis ullamcorper augue.</div>
    <div class="card-author">Mr Alden Frey</div>
    <div class="card-date">12th August 2013</div>
    <div class="card-foot"><svg width="11" height="7" viewBox="0 0 11 7"><path d="M0 3.5Q5.5-2 11 3.5Q5.5 9 0 3.5z" fill="#666"/><circle cx="5.5" cy="3.5" r="1.6" fill="#fff"/></svg>102 <svg style="margin-left:6px" width="9" height="9" viewBox="0 0 10 10"><polygon points="5,0 6.3,3.5 10,3.6 7,5.9 8.1,9.6 5,7.4 1.9,9.6 3,5.9 0,3.6 3.7,3.5" fill="#666"/></svg>3.6<span class="price">75$</span></div>
  </article>

  <article class="abs card" style="left:705px">
    <div class="card-media" style="background:var(--accent-soft)"><span class="card-plus">+</span>
      <svg width="34" height="30" viewBox="0 0 34 30"><path d="M4 12h4v14H4zM11 6h4v20h-4zM18 14h4v12h-4zM25 2h4v24h-4z" fill="#fff"/><path d="M1 28h32" stroke="#fff" stroke-width="2"/></svg></div>
    <div class="card-title">Cras scelerisque et ante eget lacinia iaculis ullamcorper augue.</div>
    <div class="card-author">Mr Alden Frey</div>
    <div class="card-date">12th August 2013</div>
    <div class="card-foot"><svg width="11" height="7" viewBox="0 0 11 7"><path d="M0 3.5Q5.5-2 11 3.5Q5.5 9 0 3.5z" fill="#666"/><circle cx="5.5" cy="3.5" r="1.6" fill="#fff"/></svg>102 <span style="margin-left:14px">3.6</span><svg width="9" height="9" viewBox="0 0 10 10"><polygon points="5,0 6.3,3.5 10,3.6 7,5.9 8.1,9.6 5,7.4 1.9,9.6 3,5.9 0,3.6 3.7,3.5" fill="#666"/></svg><span class="price">75$</span></div>
  </article>

  <div class="abs dot" style="left:518px"></div>
  <div class="abs dot" style="left:534px"></div>
  <div class="abs dot" style="left:550px"></div>
</section>

</body>
</html>
```